Quietly Orchard Honey Labels

We are an importer and distributor in the UK of fine foods from Spain. We sell primarily to the retail and wholesale trade. I need a design for wrap around labels to put on jars for four different varieties of honey - Creamy Spring Blossom, Lavender, Wild Forest and Wild Thyme. The honey originates from Spain and will primarily be sold online and to independent retailers. The look and feeling I am looking for is classical, traditional, artisan and natural. I am looking for something simple and not too fussy. There needs to be an immediate obvious distinction on each label between the 4 varieties of honey, ideally by the use of different colours in some way in each design, though I would prefer the label background to be predominantly white. It is not necessary in the design to make it evident that it is from Spain. I have attached images of the jars and the honeys and also an image of the current label just for reference (but do not refer to the design). I have also attached the text for each variety of honey. The measurements for the labels are as follows: 167mm wide and 82mm high. Our logo will go on top of the lid of the jar. I really like the design I have attached to my brief. It is labelled 'Honey Design'.

Target Market(s)

Independent food retailers and online consumers

Industry/Entity Type

Fine Foods

Font styles to use
Script
Other font styles liked:
• Freeland Font for the word Honey

Requirements
Must have
• It needs to be immediately obvious by sight that each of the 4 varieties of honey are different
Nice to have
• Just the one same icon on each label for each variety of honey. Simple. Not too fussy. I really like the design attached labelled 'honey font'.

```html
<!DOCTYPE html>
<html lang="en">
<head>
<meta charset="utf-8">
<title>Quietly Orchard Honey Labels</title>
<link rel="stylesheet" href="https://fonts.googleapis.com/css2?family=Nunito+Sans:wght@300;400;600&family=Roboto+Condensed:wght@400;700&display=swap">
<style>
  :root {
    --paper: #ffffff;
    --label-white: #f7f7f4;
    --ink: #5b5b5b;
    --ink-dark: #222222;
    --lavender: #7a5877;
    --lavender-light: #a98fa7;
    --thyme: #d7a445;
    --thyme-light: #e9c789;
    --spring: #c4664e;
    --spring-light: #dfa08c;
    --forest: #7a957a;
    --forest-light: #a9bca8;
  }
  * { box-sizing: border-box; margin: 0; padding: 0; }
  html, body { width: 1200px; height: 589px; overflow: hidden; background: var(--paper); }
  body { font-family: "Nunito Sans", sans-serif; }
  .label-sheet {
    position: relative; width: 1200px; height: 589px;
    display: grid; grid-template-columns: 540px 540px; grid-template-rows: 265px 265px;
    gap: 20px 40px; padding: 19px 40px;
  }
  .label {
    position: relative; width: 540px; height: 265px; overflow: hidden;
    background: var(--label-white);
    box-shadow: 0 1px 4px rgba(0,0,0,0.12);
  }
  .label--lavender { --tone: var(--lavender); --tone-light: var(--lavender-light); }
  .label--thyme { --tone: var(--thyme); --tone-light: var(--thyme-light); }
  .label--spring { --tone: var(--spring); --tone-light: var(--spring-light); }
  .label--forest { --tone: var(--forest); --tone-light: var(--forest-light); }

  .band-top, .band-bottom {
    position: absolute; left: 0; right: 0;
    background: linear-gradient(90deg, var(--tone) 0%, var(--tone-light) 70%, var(--tone) 100%);
  }
  .band-top { top: 0; height: 48px; }
  .band-bottom { bottom: 0; height: 12px; }

  .brand-tab {
    position: absolute; left: 195px; top: 0; width: 150px; height: 144px;
    background: var(--tone); border-radius: 0 0 4px 4px;
    text-align: center; color: #fff;
  }
  .brand-tab__eyebrow {
    margin-top: 20px; font-size: 15px; font-weight: 400; letter-spacing: 1.5px;
  }
  .brand-tab__wordmark {
    position: absolute; left: 16px; top: 52px; width: 118px; height: 74px;
    background: linear-gradient(180deg, rgba(255,255,255,0.28), rgba(255,255,255,0.14));
    border-radius: 3px;
  }

  .variety {
    position: absolute; left: 195px; top: 150px; width: 150px; text-align: center;
    color: var(--tone);
  }
  .variety__name {
    font-size: 22px; font-weight: 300; line-height: 1.2; letter-spacing: 0.3px;
  }
  .variety__rule {
    width: 76px; height: 1px; margin: 8px auto 6px; background: var(--tone);
  }
  .variety__tagline {
    font-size: 10.5px; font-weight: 400; line-height: 1.35; letter-spacing: 0.4px;
  }

  .botanical {
    position: absolute; top: 142px; width: 56px; height: 108px; border-radius: 28px 28px 6px 6px;
    background: linear-gradient(180deg, var(--tone-light), var(--tone));
    opacity: 0.55;
  }
  .botanical--left { left: 140px; }
  .botanical--right { left: 346px; }

  .care-panel {
    position: absolute; left: 14px; top: 62px; width: 118px;
    font-size: 8.5px; line-height: 1.75; color: var(--ink); text-transform: uppercase;
  }
  .care-panel__contact { margin-top: 12px; }

  .nutrition {
    position: absolute; left: 392px; top: 58px; width: 134px; height: 182px;
    border: 1px solid var(--ink-dark); padding: 4px 5px;
    font-family: "Roboto Condensed", sans-serif; color: var(--ink-dark); background: #fff;
  }
  .nutrition__title { font-size: 17px; font-weight: 700; line-height: 1; }
  .nutrition__serving { font-size: 6px; margin-top: 2px; }
  .nutrition__bar { height: 5px; background: var(--ink-dark); margin: 3px 0; }
  .nutrition__bar--thin { height: 1px; margin: 2px 0; }
  .nutrition__row { display: flex; justify-content: space-between; font-size: 6.5px; line-height: 1.45; }
  .nutrition__row--bold { font-weight: 700; }
  .nutrition__row--indent { padding-left: 8px; }
  .nutrition__note { font-size: 5.5px; line-height: 1.3; margin-top: 3px; }
</style>
</head>
<body>
<main class="label-sheet">

  <section class="label label--lavender" aria-label="Lavender Blossom label">
    <div class="band-top"></div>
    <div class="band-bottom"></div>
    <div class="care-panel">
      <p>Store in a cool, dry place. Do not refrigerate. Do not feed honey to infants under one year of age.</p>
      <p class="care-panel__contact">Quietly Orchard<br>United Kingdom<br>quietlyorchard.co.uk</p>
    </div>
    <div class="brand-tab">
      <p class="brand-tab__eyebrow">ARTISAN</p>
      <div class="brand-tab__wordmark" role="img" aria-label="Hand lettered word Honey in white script"></div>
    </div>
    <div class="botanical botanical--left" role="img" aria-label="Line drawing of flowering sprig and leaves"></div>
    <div class="botanical botanical--right" role="img" aria-label="Line drawing of leafy branch"></div>
    <div class="variety">
      <h2 class="variety__name">LAVENDER<br>BLOSSOM</h2>
      <div class="variety__rule"></div>
      <p class="variety__tagline">PREMIUM NATURAL<br>HONEY</p>
    </div>
    <div class="nutrition">
      <p class="nutrition__title">Nutrition Facts</p>
      <p class="nutrition__serving">Serving size 1/4 cup (38g) / Servings 8</p>
      <div class="nutrition__bar"></div>
      <div class="nutrition__row nutrition__row--bold"><span>Amount Per Serving</span></div>
      <div class="nutrition__row"><span>Calories 190 Cal</span><span>Cal from Fat 0</span></div>
      <div class="nutrition__bar"></div>
      <div class="nutrition__row nutrition__row--bold"><span>Total Fat 15g</span></div>
      <div class="nutrition__row nutrition__row--bold"><span>Cholesterol 10mg</span></div>
      <div class="nutrition__row nutrition__row--bold"><span>Sodium 10mg</span></div>
      <div class="nutrition__row nutrition__row--bold"><span>Total Carbohydrate 10g</span></div>
      <div class="nutrition__row nutrition__row--indent"><span>Sugar 10g</span></div>
      <div class="nutrition__row nutrition__row--bold"><span>Protein 5g</span></div>
      <div class="nutrition__bar"></div>
      <div class="nutrition__row"><span>Vitamin A</span><span>5%</span></div>
      <div class="nutrition__row"><span>Calcium</span><span>5%</span></div>
      <div class="nutrition__bar nutrition__bar--thin"></div>
      <p class="nutrition__note">* Percent Daily Values are based on a 2,000 calorie diet. Your daily values may be higher or lower depending on your calorie needs.</p>
    </div>
  </section>

  <section class="label label--thyme" aria-label="Wild Thyme label">
    <div class="band-top"></div>
    <div class="band-bottom"></div>
    <div class="care-panel">
      <p>Store in a cool, dry place. Do not refrigerate. Do not feed honey to infants under one year of age.</p>
      <p class="care-panel__contact">Quietly Orchard<br>United Kingdom<br>quietlyorchard.co.uk</p>
    </div>
    <div class="brand-tab">
      <p class="brand-tab__eyebrow">ARTISAN</p>
      <div class="brand-tab__wordmark" role="img" aria-label="Hand lettered word Honey in white script"></div>
    </div>
    <div class="botanical botanical--left" role="img" aria-label="Line drawing of flowering sprig and leaves"></div>
    <div class="botanical botanical--right" role="img" aria-label="Line drawing of leafy branch"></div>
    <div class="variety">
      <h2 class="variety__name">WILD<br>THYME</h2>
      <div class="variety__rule"></div>
      <p class="variety__tagline">PREMIUM NATURAL<br>HONEY</p>
    </div>
    <div class="nutrition">
      <p class="nutrition__title">Nutrition Facts</p>
      <p class="nutrition__serving">Serving size 1/4 cup (38g) / Servings 8</p>
      <div class="nutrition__bar"></div>
      <div class="nutrition__row nutrition__row--bold"><span>Amount Per Serving</span></div>
      <div class="nutrition__row"><span>Calories 190 Cal</span><span>Cal from Fat 0</span></div>
      <div class="nutrition__bar"></div>
      <div class="nutrition__row nutrition__row--bold"><span>Total Fat 15g</span></div>
      <div class="nutrition__row nutrition__row--bold"><span>Cholesterol 10mg</span></div>
      <div class="nutrition__row nutrition__row--bold"><span>Sodium 10mg</span></div>
      <div class="nutrition__row nutrition__row--bold"><span>Total Carbohydrate 10g</span></div>
      <div class="nutrition__row nutrition__row--indent"><span>Sugar 10g</span></div>
      <div class="nutrition__row nutrition__row--bold"><span>Protein 5g</span></div>
      <div class="nutrition__bar"></div>
      <div class="nutrition__row"><span>Vitamin A</span><span>5%</span></div>
      <div class="nutrition__row"><span>Calcium</span><span>5%</span></div>
      <div class="nutrition__bar nutrition__bar--thin"></div>
      <p class="nutrition__note">* Percent Daily Values are based on a 2,000 calorie diet. Your daily values may be higher or lower depending on your calorie needs.</p>
    </div>
  </section>

  <section class="label label--spring" aria-label="Creamy Spring label">
    <div class="band-top"></div>
    <div class="band-bottom"></div>
    <div class="care-panel">
      <p>Store in a cool, dry place. Do not refrigerate. Do not feed honey to infants under one year of age.</p>
      <p class="care-panel__contact">Quietly Orchard<br>United Kingdom<br>quietlyorchard.co.uk</p>
    </div>
    <div class="brand-tab">
      <p class="brand-tab__eyebrow">ARTISAN</p>
      <div class="brand-tab__wordmark" role="img" aria-label="Hand lettered word Honey in white script"></div>
    </div>
    <div class="botanical botanical--left" role="img" aria-label="Line drawing of flowering sprig and leaves"></div>
    <div class="botanical botanical--right" role="img" aria-label="Line drawing of leafy branch"></div>
    <div class="variety">
      <h2 class="variety__name">CREAMY<br>SPRING</h2>
      <div class="variety__rule"></div>
      <p class="variety__tagline">PREMIUM NATURAL<br>HONEY</p>
    </div>
    <div class="nutrition">
      <p class="nutrition__title">Nutrition Facts</p>
      <p class="nutrition__serving">Serving size 1/4 cup (38g) / Servings 8</p>
      <div class="nutrition__bar"></div>
      <div class="nutrition__row nutrition__row--bold"><span>Amount Per Serving</span></div>
      <div class="nutrition__row"><span>Calories 190 Cal</span><span>Cal from Fat 0</span></div>
      <div class="nutrition__bar"></div>
      <div class="nutrition__row nutrition__row--bold"><span>Total Fat 15g</span></div>
      <div class="nutrition__row nutrition__row--bold"><span>Cholesterol 10mg</span></div>
      <div class="nutrition__row nutrition__row--bold"><span>Sodium 10mg</span></div>
      <div class="nutrition__row nutrition__row--bold"><span>Total Carbohydrate 10g</span></div>
      <div class="nutrition__row nutrition__row--indent"><span>Sugar 10g</span></div>
      <div class="nutrition__row nutrition__row--bold"><span>Protein 5g</span></div>
      <div class="nutrition__bar"></div>
      <div class="nutrition__row"><span>Vitamin A</span><span>5%</span></div>
      <div class="nutrition__row"><span>Calcium</span><span>5%</span></div>
      <div class="nutrition__bar nutrition__bar--thin"></div>
      <p class="nutrition__note">* Percent Daily Values are based on a 2,000 calorie diet. Your daily values may be higher or lower depending on your calorie needs.</p>
    </div>
  </section>

  <section class="label label--forest" aria-label="Wild Forest label">
    <div class="band-top"></div>
    <div class="band-bottom"></div>
    <div class="care-panel">
      <p>Store in a cool, dry place. Do not refrigerate. Do not feed honey to infants under one year of age.</p>
      <p class="care-panel__contact">Quietly Orchard<br>United Kingdom<br>quietlyorchard.co.uk</p>
    </div>
    <div class="brand-tab">
      <p class="brand-tab__eyebrow">ARTISAN</p>
      <div class="brand-tab__wordmark" role="img" aria-label="Hand lettered word Honey in white script"></div>
    </div>
    <div class="botanical botanical--left" role="img" aria-label="Line drawing of flowering sprig and leaves"></div>
    <div class="botanical botanical--right" role="img" aria-label="Line drawing of leafy branch"></div>
    <div class="variety">
      <h2 class="variety__name">WILD<br>FOREST</h2>
      <div class="variety__rule"></div>
      <p class="variety__tagline">PREMIUM NATURAL<br>HONEY</p>
    </div>
    <div class="nutrition">
      <p class="nutrition__title">Nutrition Facts</p>
      <p class="nutrition__serving">Serving size 1/4 cup (38g) / Servings 8</p>
      <div class="nutrition__bar"></div>
      <div class="nutrition__row nutrition__row--bold"><span>Amount Per Serving</span></div>
      <div class="nutrition__row"><span>Calories 190 Cal</span><span>Cal from Fat 0</span></div>
      <div class="nutrition__bar"></div>
      <div class="nutrition__row nutrition__row--bold"><span>Total Fat 15g</span></div>
      <div class="nutrition__row nutrition__row--bold"><span>Cholesterol 10mg</span></div>
      <div class="nutrition__row nutrition__row--bold"><span>Sodium 10mg</span></div>
      <div class="nutrition__row nutrition__row--bold"><span>Total Carbohydrate 10g</span></div>
      <div class="nutrition__row nutrition__row--indent"><span>Sugar 10g</span></div>
      <div class="nutrition__row nutrition__row--bold"><span>Protein 5g</span></div>
      <div class="nutrition__bar"></div>
      <div class="nutrition__row"><span>Vitamin A</span><span>5%</span></div>
      <div class="nutrition__row"><span>Calcium</span><span>5%</span></div>
      <div class="nutrition__bar nutrition__bar--thin"></div>
      <p class="nutrition__note">* Percent Daily Values are based on a 2,000 calorie diet. Your daily values may be higher or lower depending on your calorie needs.</p>
    </div>
  </section>

</main>
</body>
</html>
```